Bref créative
Stationary and Business cards for Criminal Defense Firm
Daniel R. Halvorsen - Attorney at Law
Professional
Daniel R Halvorsen
418 N. 7th Street
Columbus, OH 43207
Daniel@verdictwithhalvorsen.example
VerdictWithHalvorsen.example

```html
<!DOCTYPE html>
<html lang="en">
<head>
<meta charset="utf-8">
<title>Daniel R Halvorsen – Stationery</title>
<link href="https://fonts.googleapis.com/css2?family=Cinzel:wght@600&family=Open+Sans:wght@400;600&display=swap" rel="stylesheet">
<style>
:root{
  --navy:#2b2768;
  --ink:#3b3b3f;
  --grey:#8a8b8f;
  --rule:#d9d9dc;
  --paper:#ffffff;
  --backdrop:#a7a8ab;
  --card-dark:#2e2e31;
  --watermark:#eeeef0;
}
*{box-sizing:border-box;margin:0;padding:0}
html,body{width:1200px;height:669px;overflow:hidden}
body{background:var(--backdrop);position:relative;font-family:"Open Sans",Arial,sans-serif;color:var(--ink)}
.piece{position:absolute;background:var(--paper);box-shadow:0 2px 8px rgba(0,0,0,.25);overflow:hidden}
.brand{display:flex;align-items:center;gap:6px;font-family:"Cinzel",Georgia,serif;font-weight:600;color:var(--navy);letter-spacing:.04em;text-transform:uppercase}
.brand-square{background:var(--navy);flex:none}
.brand-title{font-family:"Open Sans",Arial,sans-serif;font-size:6px;letter-spacing:.18em;color:var(--grey);text-transform:uppercase}
.watermark{position:absolute;font-family:"Cinzel",Georgia,serif;font-weight:600;color:var(--watermark);text-transform:uppercase;line-height:1}
.footer-band{position:absolute;left:0;right:0;bottom:0;height:22px;border-top:3px solid var(--navy);display:flex;align-items:center;justify-content:center;gap:12px;font-size:5.5px;color:var(--grey)}

/* letterhead */
.letterhead{left:450px;top:36px;width:300px;height:404px}
.letterhead .brand{position:absolute;left:22px;top:22px;font-size:10px}
.letterhead .brand-square{width:14px;height:14px}
.letterhead .brand-title{position:absolute;left:42px;top:40px}
.letter-body{position:absolute;left:22px;top:70px;width:256px;font-size:5.5px;line-height:1.6;color:var(--ink)}
.letter-body p{margin-bottom:7px}
.signature{width:60px;height:16px;background:linear-gradient(90deg,#c8cde8,#e3e6f4);border-radius:3px;margin:4px 0 2px}
.letterhead .watermark{right:-12px;bottom:34px;font-size:46px}

/* fax sheet */
.fax{left:120px;top:56px;width:290px;height:384px}
.fax .brand{position:absolute;left:20px;top:22px;font-size:9px}
.fax .brand-square{width:12px;height:12px}
.fax-heading{position:absolute;right:22px;top:22px;font-size:13px;letter-spacing:.3em;color:var(--grey);font-weight:600}
.fax-form{position:absolute;left:20px;right:20px;top:64px}
.fax-row{display:flex;align-items:flex-end;height:22px;border-bottom:1px solid var(--rule);font-size:6px;color:var(--grey)}
.fax-row span{width:36px;background:#f0f0f2;padding:3px 4px;color:var(--navy);font-weight:600}
.fax-notes{margin-top:12px;height:150px;border:1px solid var(--rule);position:relative}
.fax-notes span{position:absolute;left:0;top:0;background:#f0f0f2;padding:3px 4px;font-size:6px;color:var(--navy);font-weight:600}

/* continuation sheet */
.sheet{left:790px;top:36px;width:280px;height:370px}
.sheet .brand{position:absolute;left:20px;top:22px;font-size:9px}
.sheet .brand-square{width:12px;height:12px}
.sheet .watermark{right:-10px;bottom:32px;font-size:42px}

/* envelope */
.envelope{left:60px;top:468px;width:360px;height:170px}
.envelope .brand{position:absolute;left:18px;top:16px;font-size:8px}
.envelope .brand-square{width:11px;height:11px}
.envelope-return{position:absolute;left:35px;top:32px;font-size:5.5px;line-height:1.5;color:var(--grey)}
.envelope-flap{position:absolute;left:0;bottom:0;width:100%;height:40px}
.envelope-window{position:absolute;left:140px;top:70px;width:150px;height:44px;border:1px solid var(--rule);border-radius:3px}

/* business cards */
.card{width:214px;height:122px}
.card-front .brand{position:absolute;left:16px;top:18px;font-size:9px}
.card-front .brand-square{width:12px;height:12px}
.card-front .brand-title{position:absolute;left:34px;top:34px}
.card-contact{position:absolute;left:16px;bottom:30px;font-size:5.8px;line-height:1.55;color:var(--ink)}
.card-front .footer-band{height:14px}
.card-front.a{left:450px;top:470px}
.card-front.b{left:926px;top:440px}
.card-back{left:688px;top:500px;background:var(--card-dark)}
.card-back .brand{position:absolute;left:0;right:0;top:48px;justify-content:center;color:#fff;font-size:10px}
.card-back .brand-square{width:13px;height:13px;background:#fff}
</style>
</head>
<body>

<section class="piece fax" aria-label="Fax cover sheet">
  <div class="brand"><span class="brand-square"></span>Daniel R Halvorsen</div>
  <div class="fax-heading">FAX</div>
  <div class="fax-form">
    <div class="fax-row"><span>To:</span></div>
    <div class="fax-row"><span>From:</span></div>
    <div class="fax-row"><span>Date:</span></div>
    <div class="fax-row"><span>Pages:</span></div>
    <div class="fax-row"><span>Re:</span></div>
    <div class="fax-notes"><span>Notes:</span></div>
  </div>
  <div class="footer-band"><span>418 N. 7th Street, Columbus, OH 43207</span><span>VerdictWithHalvorsen.example</span></div>
</section>

<section class="piece letterhead" aria-label="Letterhead">
  <div class="watermark">Halvorsen</div>
  <div class="brand"><span class="brand-square"></span>Daniel R Halvorsen</div>
  <div class="brand-title">Attorney at Law</div>
  <div class="letter-body">
    <p>March 4, 2024</p>
    <p>Mr. Samuel Orton<br>210 Elm Avenue<br>Columbus, OH 43210</p>
    <p>Dear Mr. Orton,</p>
    <p>Thank you for meeting with our office this week. We have reviewed the file and prepared a plan for the next hearing.</p>
    <p>Please keep all documents related to the case and contact us before speaking with anyone about it.</p>
    <p>Sincerely,</p>
    <div class="signature" role="img" aria-label="Handwritten signature"></div>
    <p>Daniel R. Halvorsen - Attorney at Law</p>
  </div>
  <div class="footer-band"><span>418 N. 7th Street, Columbus, OH 43207</span><span>614.555.0142</span><span>VerdictWithHalvorsen.example</span></div>
</section>

<section class="piece sheet" aria-label="Second sheet">
  <div class="watermark">Halvorsen</div>
  <div class="brand"><span class="brand-square"></span>Daniel R Halvorsen</div>
  <div class="footer-band"><span>418 N. 7th Street, Columbus, OH 43207</span><span>VerdictWithHalvorsen.example</span></div>
</section>

<section class="piece envelope" aria-label="Envelope">
  <div class="brand"><span class="brand-square"></span>Daniel R Halvorsen</div>
  <div class="envelope-return">418 N. 7th Street<br>Columbus, OH 43207</div>
  <div class="envelope-window"></div>
  <svg class="envelope-flap" viewBox="0 0 360 40" preserveAspectRatio="none" aria-hidden="true">
    <path d="M0 40 L0 8 Q180 44 360 8 L360 40 Z" fill="#2e2e31"/>
  </svg>
</section>

<section class="piece card card-front a" aria-label="Business card front">
  <div class="brand"><span class="brand-square"></span>Daniel R Halvorsen</div>
  <div class="brand-title">Attorney at Law</div>
  <div class="card-contact">614.555.0142<br>Daniel@verdictwithhalvorsen.example<br>418 N. 7th Street, Columbus, OH 43207</div>
  <div class="footer-band"><span>VerdictWithHalvorsen.example</span></div>
</section>

<section class="piece card card-back" aria-label="Business card back">
  <div class="brand"><span class="brand-square"></span>Daniel R Halvorsen</div>
</section>

<section class="piece card card-front b" aria-label="Business card front">
  <div class="brand"><span class="brand-square"></span>Daniel R Halvorsen</div>
  <div class="brand-title">Attorney at Law</div>
  <div class="card-contact">614.555.0142<br>Daniel@verdictwithhalvorsen.example<br>418 N. 7th Street, Columbus, OH 43207</div>
  <div class="footer-band"><span>VerdictWithHalvorsen.example</span></div>
</section>

</body>
</html>
```